依頼詳細
レスポンシブウェブデザインを意識したデザインでお願いします。
参考URL
https://morisato-koubou.jp/

デザインに関しては、添付してあるデザインレイアウトシートを基にお願いします。

まずはパソコンサイトのデザインをお願いします。
当選後、スマホデザインをお願いします。

既存のテンプレートを使う場合は
テンプレート名を下記のような記載を提案の中にいれてください。
例:WordpressテーマはKandoria、デザインスキンは無料のHLM2019 RX4(http://kandoria.com/ex_plugin/hlmnagoya2019_rx4/)をベースにデザインいたしました。
など

素材となる写真は現在、撮影中ですので、一旦他のサイトや参考URLの写真をサンプルとして入れてください。(サンプルなどの表記をお願いします)
また、購入が必要な写真などを利用した場合は、Pelmora Stock(https://stock.pelmora.com/jp/)からファイル番号と価格を教えてください。
ページ数
1ページ
希望イメージ
シンプル 複雑
単色 カラフル
暗い 明るい
日常 高級
遊び心 厳粛
未来的 伝統的
女性的 男性的
希望する色
茶系、緑系
納品ファイル
• イラストレーター形式 (.ai)
• フォトショップ形式 (.psd)
• PNG形式 (.png)
補足説明
上記のいずれか1つ。アウトラインありとなしの2つ。

クライアントのイメージ通りでした。

たくさんのご提案ありがとうございました。
次回もぜひ、よろしくお願い致します。

```html
<!DOCTYPE html>
<html lang="ja">
<head>
<meta charset="utf-8">
<title>株式会社キサト</title>
<link href="https://fonts.googleapis.com/css2?family=Noto+Sans+JP:wght@400;500;700&family=Noto+Serif+JP:wght@500;700&family=Yuji+Syuku&display=swap" rel="stylesheet">
<style>
:root{
  --green:#2f9a4c;
  --green-dark:#237a3a;
  --brown:#7a4a1f;
  --ink:#2a2016;
  --text:#3a3a3a;
  --muted:#777;
  --cream:#fcfbe8;
  --circle:#f3edd0;
  --line:#e2ddcf;
  --footer:#deeedd;
  --qbox:#e6e6e6;
}
*{margin:0;padding:0;box-sizing:border-box}
html,body{width:1200px;height:4848px;overflow:hidden}
body{font-family:"Noto Sans JP",sans-serif;color:var(--text);background:#fff;position:relative;font-size:13px}
.abs{position:absolute}
.brand{display:flex;align-items:center;gap:10px;color:var(--green-dark);font-weight:700;font-size:26px;letter-spacing:2px}
.brand small{font-size:13px;letter-spacing:1px}
.brand .mark{width:22px;height:22px;background:var(--green);border-radius:4px}
.nav{display:flex;gap:34px;font-size:12px;color:var(--text)}
.photo{border-radius:2px}
.hero{position:absolute;left:80px;top:108px;width:1032px;height:544px;background:linear-gradient(135deg,#c7a47c,#9a7650 50%,#b8936a)}
.hero-copy{position:absolute;font-family:"Yuji Syuku",serif;color:var(--ink);text-shadow:0 0 6px rgba(255,255,255,.85);white-space:nowrap;transform:rotate(-4deg);transform-origin:left center}
.sec-title{position:absolute;left:0;width:1200px;text-align:center;font-family:"Noto Serif JP",serif;font-weight:700;color:var(--brown);font-size:22px;letter-spacing:2px}
.sec-title::before{content:"";position:absolute;left:50%;top:50%;width:110px;height:110px;margin:-55px 0 0 -55px;border-radius:50%;background:var(--circle);z-index:-1}
.band{position:absolute;left:0;width:1200px;background:var(--cream);z-index:-2}
.card{position:absolute;width:216px}
.card .photo{width:216px;height:172px}
.card h3{font-size:13px;font-weight:500;margin:20px 0 8px 8px}
.card p{font-size:11px;color:var(--muted);line-height:1.8;margin-left:8px}
.btn{display:inline-flex;align-items:center;gap:8px;background:var(--green);color:#fff;font-size:11px;padding:7px 16px;border-radius:2px}
.btn::after{content:"›";font-size:14px;line-height:1}
.strength{position:absolute;width:176px}
.strength .photo{height:136px}
.strength p{font-size:11px;line-height:1.8;margin-top:14px;text-align:center}
.case{position:absolute;width:216px;text-align:center}
.case .photo{height:168px}
.case h3{font-size:12px;font-weight:500;margin:16px 0 6px;letter-spacing:3px}
.case p{font-size:11px;color:var(--muted);line-height:1.8}
.news{position:absolute;left:290px;width:620px;font-size:12px}
.news li{list-style:none;display:flex;gap:40px;padding:22px 0;border-bottom:1px solid var(--line)}
.news time{width:80px;color:var(--muted)}
.news .ttl{width:70px}
.faq{position:absolute;left:290px;width:620px}
.faq .q,.faq .a{display:flex;align-items:flex-start;gap:16px;font-size:12px;line-height:1.9}
.faq .q{background:var(--qbox);padding:10px 14px}
.faq .a{padding:14px 14px 0}
.faq .ic{flex:none;width:26px;height:26px;border-radius:50%;color:#fff;font-size:12px;font-weight:700;display:flex;align-items:center;justify-content:center}
.faq .q .ic{background:var(--green)}
.faq .a .ic{background:var(--brown)}
.contact-line{font-size:15px;color:var(--text);letter-spacing:1px}
.contact-line b{font-size:11px;margin-right:10px;color:var(--muted);font-weight:500}
.footer{position:absolute;left:0;top:4712px;width:1200px;height:136px;background:var(--footer)}
.to-top{position:absolute;right:120px;top:88px;width:32px;height:32px;border-radius:50%;background:var(--green);display:flex;align-items:center;justify-content:center}
</style>
</head>
<body>

<header>
  <div class="abs brand" style="left:496px;top:28px"><span class="mark"></span><small>株式会社</small>キサト</div>
  <nav class="abs nav" style="left:262px;top:68px">
    <span>会社概要</span><span>弊社の強み</span><span>事業案内</span><span>加工事例・商品紹介</span><span>お知らせ</span><span>ブログ</span><span>よくある質問</span><span>お問い合わせ</span>
  </nav>
</header>

<section class="hero">
  <div class="abs" role="img" aria-label="積み上げられた薪の断面" style="inset:0;background:linear-gradient(135deg,#c7a47c,#9a7650 50%,#b8936a)"></div>
  <p class="hero-copy" style="left:440px;top:70px;font-size:44px">木のぬくもりを暮らしへ</p>
  <p class="hero-copy" style="left:420px;top:160px;font-size:40px">人と木をつなぐものづくり</p>
  <p class="hero-copy" style="left:720px;top:262px;font-size:40px">キサト</p>
</section>

<h2 class="sec-title" style="top:738px">弊社の強み</h2>
<div class="strength" style="left:80px;top:856px"><div class="photo" role="img" aria-label="製材された木材" style="background:linear-gradient(#d9b98c,#c09a6a)"></div><p>自社製材で<br>安心・確かな品質</p></div>
<div class="strength" style="left:294px;top:856px"><div class="photo" role="img" aria-label="加工された木材部品" style="background:linear-gradient(#e8e2d6,#b9a58a)"></div><p>最新機械（ルーター）で<br>精密な加工を実現</p></div>
<div class="strength" style="left:508px;top:856px"><div class="photo" role="img" aria-label="木目の美しい板材" style="background:linear-gradient(#d6b27a,#b88c52)"></div><p>木製パネルで加工</p></div>
<div class="strength" style="left:722px;top:856px"><div class="photo" role="img" aria-label="倉庫に並ぶ木材" style="background:linear-gradient(#8f7a60,#5e4d3a)"></div><p>豊富な在庫で<br>短納期に対応</p></div>
<div class="strength" style="left:936px;top:856px"><div class="photo" role="img" aria-label="木製パレット" style="background:linear-gradient(#d4b58a,#a88358)"></div><p>木の家・加工品</p></div>

<div class="band" style="top:1160px;height:640px"></div>
<h2 class="sec-title" style="top:1202px">事業案内</h2>
<div class="card" style="left:88px;top:1308px"><div class="photo" role="img" aria-label="製材された木材の断面" style="background:linear-gradient(#e3c99a,#c9a46d)"></div><h3>製材</h3><p>テキスト、テキスト<br>テキスト、テキスト</p><div style="margin:14px 0 0 8px"><span class="btn">詳細はこちら</span></div></div>
<div class="card" style="left:352px;top:1308px"><div class="photo" role="img" aria-label="工場での木材加工の様子" style="background:linear-gradient(#5a4a2a,#8a6a2a)"></div><h3>加工・販売</h3><p>テキスト、テキスト<br>テキスト、テキスト</p><div style="margin:14px 0 0 8px"><span class="btn">詳細はこちら</span></div></div>
<div class="card" style="left:620px;top:1308px"><div class="photo" role="img" aria-label="加工機械" style="background:linear-gradient(#8a8c86,#5d6058)"></div><h3>設計</h3><p>テキスト、テキスト<br>テキスト、テキスト</p><div style="margin:14px 0 0 8px"><span class="btn">詳細はこちら</span></div></div>
<div class="card" style="left:888px;top:1308px"><div class="photo" role="img" aria-label="屋外の木造あずまや" style="background:linear-gradient(#9fc3c9,#a07a4e 60%,#6f8a4a)"></div><h3>オーダーメイド</h3><p>テキスト、テキスト<br>テキスト、テキスト</p><div style="margin:14px 0 0 8px"><span class="btn">詳細はこちら</span></div></div>

<h2 class="sec-title" style="top:1850px">加工事例・商品紹介</h2>
<div class="case" style="left:88px;top:1972px"><div class="photo" role="img" aria-label="芝生の上の木製品" style="background:linear-gradient(#6a8f3a,#4f7128)"></div><h3>タイトル</h3><p>テキスト、テキスト<br>テキスト、テキスト</p></div>
<div class="case" style="left:352px;top:1972px"><div class="photo" role="img" aria-label="木工作業の様子" style="background:linear-gradient(#8a7a6a,#5a4a3a)"></div><h3>タイトル</h3><p>テキスト、テキスト<br>テキスト、テキスト</p></div>
<div class="case" style="left:620px;top:1972px"><div class="photo" role="img" aria-label="木製の加工品" style="background:linear-gradient(#c9c4b8,#9a8f7c)"></div><h3>タイトル</h3><p>テキスト、テキスト<br>テキスト、テキスト</p></div>
<div class="case" style="left:888px;top:1972px"><div class="photo" role="img" aria-label="木製の看板" style="background:linear-gradient(#d8c08a,#b49460)"></div><h3>タイトル</h3><p>テキスト、テキスト<br>テキスト、テキスト</p></div>

<div class="band" style="top:2300px;height:480px"></div>
<h2 class="sec-title" style="top:2390px">お知らせ</h2>
<ul class="news" style="top:2500px">
  <li><time>2020.00.01</time><span class="ttl">タイトル</span><span>テキスト、テキスト、テキスト、テキスト、テキスト</span></li>
  <li><time>2020.00.01</time><span class="ttl">タイトル</span><span>テキスト、テキスト、テキスト、テキスト、テキスト</span></li>
  <li><time>2020.00.01</time><span class="ttl">タイトル</span><span>テキスト、テキスト、テキスト、テキスト、テキスト</span></li>
</ul>
<span class="abs btn" style="left:1000px;top:2744px">記事一覧</span>

<h2 class="sec-title" style="top:2934px">ブログ</h2>
<div class="case" style="left:88px;top:3048px"><div class="photo" role="img" aria-label="木製の表札" style="height:172px;background:linear-gradient(#d8b888,#b8925c)"></div><p style="margin-top:16px">2020.00.01</p><h3 style="margin-top:2px">タイトル</h3></div>
<div class="case" style="left:352px;top:3048px"><div class="photo" role="img" aria-label="緑の中の木製看板" style="height:172px;background:linear-gradient(#8fb86a,#d8c8a0 50%,#6f9a4a)"></div><p style="margin-top:16px">2020.00.01</p><h3 style="margin-top:2px">タイトル</h3></div>
<div class="case" style="left:620px;top:3048px"><div class="photo" role="img" aria-label="屋外の案内看板" style="height:172px;background:linear-gradient(#6f9a5a,#8a6a3a)"></div><p style="margin-top:16px">2020.00.01</p><h3 style="margin-top:2px">タイトル</h3></div>
<div class="case" style="left:888px;top:3048px"><div class="photo" role="img" aria-label="木製の巣箱" style="height:172px;background:linear-gradient(#e8ddc8,#c4a070)"></div><p style="margin-top:16px">2020.00.01</p><h3 style="margin-top:2px">タイトル</h3></div>
<span class="abs btn" style="left:1000px;top:3344px">記事一覧</span>

<div class="band" style="top:3440px;height:560px"></div>
<h2 class="sec-title" style="top:3534px">よくある質問</h2>
<div class="faq" style="top:3636px">
  <div class="q"><span class="ic">Q</span><span>〇〇はありますか？</span></div>
  <div class="a"><span class="ic">A</span><span>ありますが、どんなものでも、あり、形状もあります。<br>製品、資料をイラストなどご用意しております。お気軽にお問い合わせください。</span></div>
  <div class="q" style="margin-top:28px"><span class="ic">Q</span><span>〇〇はどのくらいかかりますか？</span></div>
  <div class="a"><span class="ic">A</span><span>さい、ものが、大きさと、数量、デザインなど……<br>ご一緒にお見積もりいたしますので、お気軽にどうぞ。</span></div>
</div>
<span class="abs btn" style="left:1000px;top:3930px">一覧を見る</span>

<h2 class="sec-title" style="top:4094px">お問い合わせ</h2>
<div class="abs photo" role="img" aria-label="社名が書かれた木製の看板" style="left:292px;top:4224px;width:288px;height:340px;background:linear-gradient(#e6d3ae,#cdb182)"></div>
<p class="abs contact-line" style="left:624px;top:4300px"><b>TEL</b>0276-55-2840</p>
<p class="abs contact-line" style="left:624px;top:4386px"><b>MAIL</b>info@kisato-mokuzai.jp</p>
<span class="abs btn" style="left:636px;top:4436px;font-size:13px;padding:12px 26px">お問い合わせフォーム</span>

<footer class="footer">
  <nav class="abs nav" style="left:262px;top:22px">
    <span>会社概要</span><span>弊社の強み</span><span>事業案内</span><span>加工事例・商品紹介</span><span>お知らせ</span><span>ブログ</span><span>よくある質問</span><span>お問い合わせ</span>
  </nav>
  <div class="abs brand" style="left:496px;top:62px"><span class="mark"></span><small>株式会社</small>キサト</div>
  <div class="to-top"><svg width="12" height="12" viewBox="0 0 12 12"><path d="M2 8 L6 4 L10 8" stroke="#fff" stroke-width="2" fill="none"/></svg></div>
</footer>

</body>
</html>
```